Yoga/movement guide/teacher for adult yoga practice and kid yoga

What is the positioning or mission statement of your company? to guide individuals in a yoga-based safe and sustainable movement practice applicable to all ages and body types. Currently my focus is working with children in daycare and school settings, but my goal is to expand into private yoga practice for adults, and potentially as part of rented space in studios. I hope to find a way to work with children AND adults (so would love for logo to be appealing to both), but current focus is with children based on need and demand in the community. yoga for children also compliments my backround as a pediatrician/neonatologist, and I greatly miss interacting with children. I also want to emphasize a yoga/movement practice that is focused more on what one feels internally through movement. NOT what one looks like asthetically. I believe in removing all mirrors from yoga/movement practice. It should be an experience of movement/poses/yoga through appropriate cueing and education. It is not about the details of how far the knee should bend, or how high the leg should be. Focusing on foudation first, core, then core engagement and ultimately expression of poses/movements. A focus on strength, stability and mobility, not just flexibility, which is the common perception/association with yoga. I also want individuals to learn to be an advocate of their own health. Through guidance, I hope for individuals to connect with their body so they know themselves so well to be able to advocate for themselves in the modern healthcare world. This internal experience and connection is so essential in a world where modern medicine has become a business and it is all about making a dollar. the connection with patients is lost, and individuals need to learn to empower themselves and through their new found voice to be able to articulate what is wrong.<br/>Does your company have a tagline or slogan that should be included with the logo? "Practice Glowing Motion"<br/>What do you hope your company can be known for? Accessible yoga for a sustained practice. A guided movement practice where one gains information and knowledge of oneself through a mind/body connection. For one feel good physically with a new awaraness of their internal radiance that exists in all beings. Physical rejuvenation egnites a light and increases energy to flow through the physical body, which ultimately tranlates into works of kindness for others and out in the world. <br/>What color palettes might you prefer? why? love the colors currently chosen<br/>Where will the logo be primarily used? initially business cards, but hopefully future websites, t-shirts, and potentially local magazine adds. Also starting with a small couple of banners for community events in the area. I currently practice as a nomad out of my car :)<br/>Are there any elements you would prefer to see in the logo? Movement. A modern depiction of a human body/figure practicing movement. Hoping to avoid a stereotypical yoga pose per say, just because I want to people to think of it more of a movement practice with yoga roots. Modern yoga. There are elements of breathing and connecting with oneself through the flow of breath and movement, but I do not focus on the meditative/cerebral aspect of the yoga practice. What I teach is almost reaching a meditative state through movement. I personally don't practice, nor resonate with just seated meditation. just not my thing :)<br/>In your opinion, what defines a well-designed logo? curiosity. enough info for individuals to think they know what it means, but want to know more. invokes curiosity, but not too abstract. Reproducible. not too complicated. I want also to invoke a community feel, so a design that appeals to all people within a community. <br/>What is your preference in reference to icons, typography, spokespeople (characters), etc.? modern design. I love the idea of a logo for my purposes, to invoke a sense of movement from within. So not too static. <br/>What words or icons must be included in the logo? movement with yoga roots. <br/>What logos do you like and why? A representation, but not exact. I think some ambiguity is intriguing for others, and also memorable. I want it to be an artistic representation of movement/yoga<br/>What logos do you dislike and why? too busy, too loud. <br/>In your opinion, what is the primary purpose for a logo? association<br/>Who is the primary target audience? (who is most likely to use your services/product?) Children and their parents, but ultimately to expand into teaching adults. I even have aspirations of prenatal and post-natal yoga. Potentially incorporating infants. <br/>Who currently uses your product the most? n/a (working in schools/daycare currently. It is currently all volunteer)<br/>Are you pleased with the range of people your company serves? n/a<br/>Are you looking to expand, modify, or completely change your target audience? or will it remain the same? yes! expand into an adult audience. <br/>How do you plan to focus on your target audience? currently by working through schools and daycares. hopefully ultimately through after school care programs and then offering kid yoga in an existing yoga studio (working on this with Q Loft in Ridgeland, currently)<br/>What are your main forms of advertising? word of mouth, schools, daycares. Happy kids talking to their parents about the yoga class they took and happy teachers :)<br/>How do most customers find out about your company?<br/>Which gender are you targeting? All genders! However, with kid yoga, often the maternal individual in the child's life is more involved with decision making as far as extracurricular activities

Target Market(s)

individuals and families interested in wellness and feeling great

Contact Information for Business Card

Dana Whitmore
Yoga Instructor
RYT-200, RCYT

certified yoga teacher for adults and children

Colors

Designer to choose colors to be used in the design.

Requirements
Must have
• "Practice Glowing Motion"
Nice to have
• logo with same colors

```html
<!DOCTYPE html>
<html lang="en">
<head>
<meta charset="utf-8">
<title>Brightway Studios – Business Card</title>
<link rel="stylesheet" href="https://fonts.googleapis.com/css2?family=Amatic+SC:wght@400&family=Archivo:wght@600&family=Lato:wght@300;400&display=swap">
<style>
  :root {
    --backdrop: #2c2c2c;
    --card-white: #ffffff;
    --sun-yellow: #f5d93e;
    --deep-yellow: #e3c51a;
    --aqua: #62c9d0;
    --ink: #333333;
    --logo-grey: #6d6d6d;
    --rule-grey: #9a9a9a;
  }
  * { box-sizing: border-box; margin: 0; padding: 0; }
  html, body {
    width: 1200px; height: 1200px; overflow: hidden;
    background: var(--backdrop);
  }
  .stage { position: relative; width: 1200px; height: 1200px; }

  .card {
    position: absolute; top: 310px; width: 364px; height: 594px;
    box-shadow: 2px 3px 6px rgba(0,0,0,0.55);
  }
  .card--front { left: 234px; background: var(--card-white); }
  .card--back {
    left: 627px; width: 369px;
    background: linear-gradient(135deg, var(--deep-yellow) 0%, var(--sun-yellow) 55%, var(--deep-yellow) 100%);
  }

  .brand {
    position: absolute; top: 40px; left: 0; width: 100%;
    text-align: center;
  }
  .brand__dot {
    display: block; width: 150px; height: 150px; margin: 0 auto;
    border-radius: 50%; background: var(--sun-yellow);
  }
  .brand__name {
    margin-top: 18px;
    font-family: "Lato", sans-serif; font-weight: 300;
    font-size: 34px; color: var(--logo-grey); letter-spacing: 0.5px;
  }

  .tagline {
    position: absolute; top: 296px; left: 0; width: 100%;
    text-align: center;
    font-family: "Amatic SC", cursive; font-size: 29px;
    letter-spacing: 3.2px; color: var(--aqua);
  }

  .contact {
    position: absolute; top: 390px; left: 0; width: 100%;
    text-align: center;
  }
  .contact__name {
    font-family: "Archivo", sans-serif; font-weight: 600;
    font-size: 21px; color: var(--sun-yellow); letter-spacing: 0.2px;
  }
  .contact__icons {
    display: flex; align-items: center; justify-content: center;
    gap: 4px; margin-top: 14px;
  }
  .contact__rule { width: 48px; height: 1px; background: var(--rule-grey); margin: 0 6px; }
  .contact__icon {
    width: 24px; height: 24px; border-radius: 50%;
    background: var(--sun-yellow);
    display: flex; align-items: center; justify-content: center;
  }
  .contact__details {
    margin-top: 12px;
    font-family: "Lato", sans-serif; font-weight: 400;
    font-size: 16.5px; line-height: 22px; color: var(--ink);
  }
</style>
</head>
<body>
<main class="stage">
  <section class="card card--front" aria-label="Business card front">
    <div class="brand">
      <span class="brand__dot"></span>
      <p class="brand__name">Brightway Studios</p>
    </div>

    <p class="tagline">PRACTICE GLOWING MOTION</p>

    <div class="contact">
      <p class="contact__name">DANA WHITMORE</p>
      <div class="contact__icons">
        <span class="contact__rule"></span>
        <span class="contact__icon">
          <svg width="14" height="14" viewBox="0 0 14 14" aria-hidden="true">
            <path d="M2 5 Q7 1 12 5 L11 7 L9 6 L9 5 Q7 4 5 5 L5 6 L3 7 Z" fill="#fff"/>
            <rect x="4" y="7.5" width="6" height="4" rx="1" fill="#fff"/>
          </svg>
        </span>
        <span class="contact__icon">
          <svg width="14" height="14" viewBox="0 0 14 14" aria-hidden="true">
            <rect x="2" y="3.5" width="10" height="7" fill="none" stroke="#fff" stroke-width="1.3"/>
            <path d="M2 3.5 L7 8 L12 3.5" fill="none" stroke="#fff" stroke-width="1.3"/>
          </svg>
        </span>
        <span class="contact__icon">
          <svg width="14" height="14" viewBox="0 0 14 14" aria-hidden="true">
            <circle cx="7" cy="7" r="5" fill="none" stroke="#fff" stroke-width="1.3"/>
            <ellipse cx="7" cy="7" rx="2.2" ry="5" fill="none" stroke="#fff" stroke-width="1"/>
            <line x1="2" y1="7" x2="12" y2="7" stroke="#fff" stroke-width="1"/>
          </svg>
        </span>
        <span class="contact__rule"></span>
      </div>
      <p class="contact__details">
        044-555 010 220<br>
        hello@brightwaystudios.com<br>
        www.brightwaystudios.com
      </p>
    </div>
  </section>

  <section class="card card--back" role="img" aria-label="Card back: enlarged brand symbol of a sun with a flowing aqua figure on yellow"></section>
</main>
</body>
</html>
```